Smart Home App Needs 4 Mockup Screens. Extra Work Guaranteed for Winner

BACKGROUND
Our company, Marlow, is launching an exciting new app early next year. And we need some examples of what our app will look like to show to some of the biggest retailers in the world. We hope that this project will lead to regular work as we have a lot of new products planned for the app.

Our app will support baby, home and pet monitors (cameras) as well as the world's first smart pet flap.

The monitors allow you to do much more than just watch live video. By monitoring and providing information on sound, movement and temperature the app provides the user with instant peace of mind wherever they are. If anything has changed the user can be alerted via notifications. If motion is detected the user will receive a clip of the whole event moments after it has happened.

The Smart Pet Flap is packed full of features too. From letting you decide when your pet can or can't go outside from your mobile, to automatically opening if a fire is detected (along with a whole host of other features) - this really is the most advanced pet flap in the world.

REQUIREMENTS
We need 4 mock-up screens creating to show the UI of our app.
1. Camera Home Page
2. Camera Notifications Page
3. Pet Flap Fire Alarm Warning Page
4. Extreme Weather Warning Page

Optional - Happy to Pay the Winner Extra for these Designs
5. Start Up/Log In Page
6. Pet Flap Notification Example
7. Pet Flap Scheduler Page (your choice)
(SEE MARLOW APP DESIGN COMPETITION - ATTACHED)

STYLE GUIDE
As you'll see from our wireframes we want our app to be very minimal and modern. The predominant colour will be white but where colour is used it should be bright (see our colour palette - which we will provide shortly).

INSPIRATION
We love the UI of Tumbleweed (home surveillance). Also check out Pike (smart thermostat).
(SEE MARLOW UI EXAMPLES ATTACHED)

LOGO
We love our logo. Feel free to use it in creative ways.

So far we're also using it as a kind of beacon to indicate if everything is ok.

LOGO COLOURS & APP COLOURS
As mentioned, we are thinking of using the green logo to indicate that everything is ok (and also for the pet app in general). We reserve red for when something has happened (normally bad) and needs attention, like a fire alarm going off.

The app will be predominantly black and white with the odd minimal flash of colour (probably primary colour)
We'll upload a colour scheme as soon as we have it.

CONTACT
Please message us for more details - we'll do our best to reply promptly.

FUTURE WORK
We will need extra screens made straight after the competition is over and there should be additional regular work after this.

Target Market(s)

Our app will be used by young professionals, to young parents to grandparents. The design must be contemporary but timeless and easy to use no matter how good you are with technology.

Industry/Entity Type

Pet

Font styles to use
Sans Serif

Colors
faee3f
33a6d7
ec1f27
acd036
32b7a4

Requirements
Must have
• Beautiful, minimal design. Make sure you spend time looking at the Tumbleweed and Pike apps before starting.

For the videos make sure you use sensible images - that you'd expect to see from a monitor (high resolution images if possible)
Nice to have
• Creative use of our logo.
Should not have
• Too much detail/clutter/colours. Ugly fonts.

```html
<!DOCTYPE html>
<html lang="en">
<head>
<meta charset="utf-8">
<title>Marlow — Earlier activity</title>
<link rel="stylesheet" href="https://fonts.googleapis.com/css2?family=Roboto:wght@300;400;500&display=swap">
<style>
  :root {
    --page-bg: #e9e6e1;
    --screen-bg: #f1f0ee;
    --status-bg: #111111;
    --ink: #2b2b2b;
    --ink-soft: #555555;
    --ink-faint: #b9b9b9;
    --rule: #dddcda;
    --timeline: #cfcfcf;
    --alert: #e0583c;
    --ok: #4cae3e;
    --tab-active: #dcdcdc;
    --white: #ffffff;
  }
  * { box-sizing: border-box; margin: 0; padding: 0; }
  html, body {
    width: 1200px; height: 900px; overflow: hidden;
    background: var(--page-bg);
    font-family: "Roboto", "Helvetica Neue", Arial, sans-serif;
  }
  .app-screen {
    position: absolute; left: 360px; top: 24px;
    width: 480px; height: 852px;
    background: var(--screen-bg);
    overflow: hidden;
    box-shadow: 0 10px 40px rgba(0,0,0,0.12);
  }
  .status-bar {
    height: 30px; background: var(--status-bg); color: var(--white);
    display: flex; align-items: center; justify-content: space-between;
    padding: 0 10px; font-size: 13px; font-weight: 500;
  }
  .status-bar .signal { display: flex; gap: 3px; }
  .status-bar .signal span { width: 6px; height: 6px; border-radius: 50%; background: var(--white); }
  .status-bar .battery { display: flex; align-items: center; gap: 4px; font-weight: 400; }
  .status-bar .battery i { display: block; width: 24px; height: 11px; border: 1px solid var(--white); border-radius: 2px; background: var(--white); background-clip: content-box; padding: 1px; }
  .tab-bar {
    height: 44px; display: flex; align-items: stretch; justify-content: flex-end;
    padding-right: 12px; border-bottom: 1px solid var(--rule);
  }
  .tab { display: flex; align-items: center; padding: 0 16px; font-size: 20px; color: var(--ink); font-weight: 300; }
  .tab.is-active { background: var(--tab-active); }
  .brand { display: flex; align-items: center; gap: 6px; margin-left: 12px; color: var(--ok); font-size: 15px; font-weight: 400; }
  .brand i { width: 10px; height: 10px; border-radius: 50%; background: var(--ok); }
  .menu-button { position: absolute; left: 26px; top: 92px; }
  .scroll-thumb { position: absolute; right: 8px; top: 90px; width: 4px; height: 110px; border-radius: 2px; background: #c9c9c9; }
  .status-summary { position: absolute; left: 150px; top: 122px; }
  .status-summary h1 { font-size: 31px; font-weight: 300; color: var(--ink); letter-spacing: -0.3px; }
  .status-summary .summary-time { font-size: 26px; font-weight: 400; color: var(--ok); margin-top: 2px; }
  .timeline-line { position: absolute; left: 100px; top: 228px; width: 2px; bottom: 0; background: var(--timeline); }
  .timeline-start { position: absolute; left: 96px; top: 224px; width: 10px; height: 10px; border-radius: 50%; background: var(--timeline); }
  .event { position: absolute; left: 0; width: 480px; height: 110px; }
  .event-rule { position: absolute; left: 200px; right: 40px; top: 0; height: 1px; background: var(--rule); }
  .event-body { position: absolute; left: 206px; top: 22px; }
  .event-time { font-size: 22px; color: var(--alert); font-weight: 400; }
  .event-room { font-size: 13px; color: var(--ink); margin-top: 2px; }
  .event-note { font-size: 12.5px; color: var(--ink-faint); margin-top: 3px; }
  .event-dot { position: absolute; left: 95px; top: 38px; width: 12px; height: 12px; border-radius: 50%; background: var(--timeline); }
  .event-thumb { position: absolute; left: 66px; top: 16px; width: 70px; height: 70px; border-radius: 50%; border: 3px solid var(--white); box-shadow: 0 1px 3px rgba(0,0,0,0.2); }
  .thumb-nursery { background: radial-gradient(circle at 45% 45%, #f1d3c6, #d9b3a4 60%, #c9cbd6); }
  .thumb-living { background: linear-gradient(160deg, #e7e2d8, #a08a6e 60%, #5e4b3a); }
  .thumb-petroom { background: linear-gradient(150deg, #ede6d6, #9a8b70 55%, #4e4434); }
  .clip-badge { position: absolute; left: 116px; top: 8px; width: 26px; height: 26px; border-radius: 50%; background: var(--alert); border: 2px solid var(--white); display: flex; align-items: center; justify-content: center; }
</style>
</head>
<body>
  <main class="app-screen">
    <div class="status-bar">
      <div class="signal"><span></span><span></span><span></span><span></span><span></span></div>
      <div class="clock">07:42 AM</div>
      <div class="battery">100% <i></i></div>
    </div>

    <nav class="tab-bar">
      <div class="tab">Now</div>
      <div class="tab is-active">Earlier</div>
      <div class="brand"><i></i>Marlow</div>
    </nav>

    <svg class="menu-button" width="28" height="22" viewBox="0 0 28 22" aria-label="Menu">
      <rect y="1" width="28" height="3" fill="#333"/>
      <rect y="9.5" width="28" height="3" fill="#333"/>
      <rect y="18" width="28" height="3" fill="#333"/>
    </svg>
    <div class="scroll-thumb"></div>

    <header class="status-summary">
      <h1>All is quiet at home</h1>
      <div class="summary-time">7:42am</div>
    </header>

    <div class="timeline-line"></div>
    <div class="timeline-start"></div>

    <section class="event" style="top:262px">
      <div class="event-rule"></div>
      <div class="event-thumb thumb-nursery" role="img" aria-label="Camera still of a baby in the nursery"></div>
      <div class="clip-badge"><svg width="14" height="11" viewBox="0 0 14 11"><rect x="0" y="2" width="14" height="9" rx="2" fill="#fff"/><rect x="4" y="0" width="6" height="3" rx="1" fill="#fff"/><circle cx="7" cy="6.5" r="2.5" fill="#e0583c"/></svg></div>
      <div class="event-body">
        <div class="event-time">07:15am</div>
        <div class="event-room">Nursery</div>
        <div class="event-note">There's a lot of movement and noise</div>
      </div>
    </section>

    <section class="event" style="top:372px">
      <div class="event-rule"></div>
      <div class="event-dot"></div>
      <div class="event-body">
        <div class="event-time">06:07am</div>
        <div class="event-room">Garden</div>
        <div class="event-note">There's some loud noise</div>
      </div>
    </section>

    <section class="event" style="top:482px">
      <div class="event-rule"></div>
      <div class="event-thumb thumb-living" role="img" aria-label="Camera still of the living room"></div>
      <div class="clip-badge"><svg width="14" height="11" viewBox="0 0 14 11"><rect x="0" y="2" width="14" height="9" rx="2" fill="#fff"/><rect x="4" y="0" width="6" height="3" rx="1" fill="#fff"/><circle cx="7" cy="6.5" r="2.5" fill="#e0583c"/></svg></div>
      <div class="event-body">
        <div class="event-time">05:32am</div>
        <div class="event-room">Living room</div>
        <div class="event-note">There's some loud noise and movement</div>
      </div>
    </section>

    <section class="event" style="top:592px">
      <div class="event-rule"></div>
      <div class="event-dot"></div>
      <div class="event-body">
        <div class="event-time">04:49am</div>
        <div class="event-room">Living room</div>
        <div class="event-note">The temperature has just dropped to 16°</div>
      </div>
    </section>

    <section class="event" style="top:702px">
      <div class="event-rule"></div>
      <div class="event-thumb thumb-petroom" role="img" aria-label="Camera still of the pet's room"></div>
      <div class="clip-badge"><svg width="14" height="11" viewBox="0 0 14 11"><rect x="0" y="2" width="14" height="9" rx="2" fill="#fff"/><rect x="4" y="0" width="6" height="3" rx="1" fill="#fff"/><circle cx="7" cy="6.5" r="2.5" fill="#e0583c"/></svg></div>
      <div class="event-body">
        <div class="event-time">04:11am</div>
        <div class="event-room">Fido's Room</div>
        <div class="event-note">There's a lot of movement</div>
      </div>
    </section>
  </main>
</body>
</html>
```